Modern Innovative Business Card Design

We require a nice, modern, clean business card design, ready for upload to Cardomora. Our company develops online banking software solutions for small financial insitutions. The design should be clean, professional, but yet not "corporate boring". See www.fyrolt.com for an idea of business image and profile. The design should communicate innovation, be modern and fresh, yet look professional and established.

Target Market(s)

Finance industry, bankers, entrepreneurs

Industry/Entity Type

Financial

Contact Information for Business Card

Tobias Wendlerup
CEO

FYROLT BV
Lindenwerf 38
1027 HX Amsterdam
The Netherlands

Phone: +31 20 517 8036
Direct: +31 20 604 1758
Skype: tobias.fyrolt
ceo@fyrolt.com
www.fyrolt.com

Font styles to use
Sans Serif

Requirements
Must have
• Should look clean, modern and professional. File should be ready for upload to cardomora.
Should not have
• Boring standard corporate layout

```html
<!DOCTYPE html>
<html lang="en">
<head>
<meta charset="utf-8">
<title>FYROLT business card</title>
<link rel="stylesheet" href="https://fonts.googleapis.com/css2?family=Open+Sans:wght@400;600;700&display=swap">
<style>
  :root {
    --green: #82c341;
    --ink: #3c3c3c;
    --grey: #5a5a5a;
    --paper: #ffffff;
    --backdrop: #e8e9eb;
  }
  * { margin: 0; padding: 0; box-sizing: border-box; }
  html, body {
    width: 1200px;
    height: 901px;
    overflow: hidden;
    background: var(--backdrop);
    font-family: "Open Sans", Arial, sans-serif;
    color: var(--ink);
  }
  .stage {
    position: relative;
    width: 1200px;
    height: 901px;
  }
  .card {
    position: absolute;
    top: 302px;
    width: 520px;
    height: 297px;
    box-shadow: 0 2px 6px rgba(0,0,0,0.12);
  }
  .card--back {
    left: 60px;
    background: var(--green);
  }
  .card--front {
    left: 620px;
    background: var(--paper);
  }
  .brand {
    position: absolute;
    left: 128px;
    top: 40px;
  }
  .brand__name {
    font-size: 34px;
    font-weight: 600;
    letter-spacing: 2px;
    color: var(--grey);
    line-height: 1;
  }
  .brand__tagline {
    font-size: 12.5px;
    color: var(--grey);
    margin-top: 3px;
  }
  .name-band {
    position: absolute;
    left: 0;
    right: 0;
    top: 106px;
    height: 30px;
    background: var(--green);
  }
  .name-band__name {
    position: absolute;
    left: 128px;
    top: 4px;
    font-size: 16px;
    font-weight: 700;
    color: var(--paper);
    letter-spacing: 0.2px;
  }
  .role {
    position: absolute;
    left: 252px;
    top: 140px;
    font-size: 15px;
    color: var(--grey);
  }
  .phones {
    position: absolute;
    right: 24px;
    top: 142px;
    font-size: 12.5px;
    line-height: 18px;
    color: var(--ink);
  }
  .phones__row { display: flex; align-items: center; gap: 4px; }
  .label { color: var(--green); }
  .icon-phone { width: 12px; height: 12px; }
  .web { font-weight: 600; color: var(--ink); }
  .details {
    position: absolute;
    left: 28px;
    bottom: 26px;
    font-size: 13px;
    line-height: 19px;
    color: var(--ink);
  }
</style>
</head>
<body>
<main class="stage">
  <section class="card card--back" aria-label="Card back"></section>

  <section class="card card--front" aria-label="Card front">
    <div class="brand">
      <div class="brand__name">FYROLT</div>
      <div class="brand__tagline">F for Finance - F for Future</div>
    </div>

    <div class="name-band">
      <span class="name-band__name">Tobias Wendlerup</span>
    </div>
    <div class="role">CEO</div>

    <div class="phones">
      <div class="phones__row">
        <svg class="icon-phone" viewBox="0 0 12 12" aria-hidden="true">
          <circle cx="6" cy="6" r="5.3" fill="none" stroke="#82c341" stroke-width="1.2"/>
          <path d="M4.3 3.4c.4-.3.8-.2 1 .2l.4.8c.1.3 0 .5-.2.7l-.3.2c.3.7.8 1.2 1.5 1.5l.2-.3c.2-.2.4-.3.7-.2l.8.4c.4.2.5.6.2 1-.5.6-1.1.8-1.8.5C5.4 7.8 4.2 6.6 3.8 5.2c-.2-.7 0-1.3.5-1.8z" fill="#82c341"/>
        </svg>
        <span>: +31 20 517 8036</span>
      </div>
      <div><span class="label">Direct:</span> +31 20 604 1758</div>
      <div class="web">www.fyrolt.com</div>
    </div>

    <div class="details">
      <div>BV Lindenwerf, 38 1027 HX</div>
      <div>Amsterdam, The Netherlands</div>
      <div><span class="label">Skype:</span> tobias.fyroltceo@fyrolt.com</div>
    </div>
  </section>
</main>
</body>
</html>
```